Wordpress Design Project SEO/SEM Website

Need an updated more professional look for an SEO/SEM existing site.
see: www.harborkite-solvex.com

I have an existing logo (in eps format), but am flexible on color and would consider updating the logo if the current colors or design limits your creativity.

Target Market(s)

My customers tend to be marketing managers for mid-size companies with 50+ employees.

Industry/Entity Type

Marketing

Requirements
Must have
• Design should support WordPress 3.0 menus, and widgets.
Nice to have
• Should you want/need it, the font used in the logo is 'ARTLOOKIN'
Should not have
• flash

```html
<!DOCTYPE html>
<html lang="en">
<head>
<meta charset="utf-8">
<title>Harborkite – Search Marketing</title>
<link href="https://fonts.googleapis.com/css2?family=Arimo:wght@400;700&family=Cinzel:wght@600&family=Tinos&family=Ubuntu:wght@400&display=swap" rel="stylesheet">
<style>
:root{
  --sky:#00a6ec;
  --sky-deep:#0b8fd0;
  --bubble:#6fd0f8;
  --white:#ffffff;
  --ink:#2b2b2b;
  --text:#444444;
  --link:#1a8fd6;
  --title-blue:#2596d6;
  --orange:#f26b1d;
  --red:#e8262d;
  --line:#cfcfcf;
}
*{box-sizing:border-box;margin:0;padding:0}
html,body{width:902px;height:1200px;overflow:hidden;background:var(--white)}
body{position:relative;font-family:"Arimo",Arial,sans-serif;color:var(--text)}
.abs{position:absolute;z-index:2}
.backdrop{z-index:0}

/* header */
.brand{left:110px;top:40px;display:flex;align-items:center;gap:8px;font-size:19px;font-weight:400;color:var(--ink);letter-spacing:1px}
.brand-dot{width:26px;height:26px;border-radius:50%;background:var(--sky)}
.social{display:flex;gap:8px}
.social span{width:28px;height:28px;border-radius:50%;background:var(--sky-deep);display:block}
.social.top{left:706px;top:35px}
.social.foot{left:692px;top:1111px}
.nav{left:225px;top:90px;height:31px;display:flex;font-size:11.5px;color:#111}
.nav a{display:flex;align-items:center;justify-content:center;height:27px;margin-top:4px;background:linear-gradient(#f4f4f4,#d9d9d9);border-right:1px solid #c8c8c8;color:#111;text-decoration:none}
.nav a.current{background:var(--sky);color:var(--white);height:31px;margin-top:0}
.search{left:662px;top:94px;width:150px;height:27px;background:linear-gradient(#f4f4f4,#d9d9d9);padding:4px 6px}
.search-box{width:100%;height:100%;background:var(--white);border:1px solid #d0d0d0;font-size:8.5px;color:#888;padding:4px 5px;position:relative}
.search-btn{position:absolute;right:-1px;top:-1px;width:19px;height:19px;background:var(--sky)}

/* hero */
.hero{left:0;top:121px;width:902px;height:318px;background:var(--sky);overflow:hidden}
.hero h1{position:absolute;left:141px;top:44px;font-family:"Cinzel",serif;font-weight:600;font-size:41px;line-height:39px;color:var(--white)}
.hero h2{position:absolute;left:141px;top:128px;font-size:22.5px;line-height:26px;font-weight:700;color:#111}
.btn-red{background:var(--red);color:var(--white);font-weight:700;display:flex;align-items:center;justify-content:center}
.hero .know{position:absolute;left:142px;top:197px;width:129px;height:40px;font-size:15.5px;letter-spacing:.3px}
.hero-photo{position:absolute;left:490px;top:40px;width:330px;height:278px;border-radius:50% 40% 0 0/55% 50% 0 0;background:linear-gradient(160deg,#6aa84f 0%,#4a3323 35%,#e9b48e 60%,#d49a74 100%)}

/* cards */
.card-photo{top:463px;width:149px;height:102px;border:2px solid #cfcfcf;border-radius:3px}
.card-text{top:575px;width:170px;font-size:10.5px;line-height:14.5px;color:#333;letter-spacing:.3px}
.btn-grey{background:linear-gradient(#fafafa,#e6e6e6);border:1px solid #cbcbcb;font-family:"Tinos",serif;color:#666;display:flex;align-items:center;justify-content:center}
.card-btn{top:617px;width:78px;height:26px;font-size:11.5px}

/* news */
.section-title{font-weight:700;color:#222}
.news-title{left:599px;top:463px;font-size:26px}
.news-sub{left:599px;top:500px;font-size:12px;color:var(--orange)}
.news-list{left:587px;top:520px;list-style:none;font-size:9px;color:#444;letter-spacing:.3px}
.news-list li{height:17.6px;padding-left:12px;position:relative}
.news-list li::before{content:">";position:absolute;left:0;color:var(--orange);font-size:8px}
.news-btn{left:596px;top:617px;width:77px;height:26px;font-family:"Tinos",serif;font-weight:400;font-size:12px}

/* about */
.about-title{left:95px;top:690px;font-size:28px;font-weight:700;color:var(--title-blue)}
.about-text{left:96px;top:730px;width:440px;font-size:12.5px;line-height:20px;letter-spacing:.5px;white-space:nowrap}
.about-text p+p{margin-top:20px}
.about-btn{left:430px;top:891px;width:80px;height:28px;font-size:12px}

/* blog */
.blog-title{left:599px;top:675px;font-size:25px}
.blog-list{left:596px;top:720px;width:196px;list-style:none;font-size:10.5px;line-height:13.5px;color:var(--link)}
.blog-list li{border-bottom:1px dashed var(--line);padding:3px 0 8px}
.blog-list li.short{padding:6px 0 10px}

/* bottom */
.footer-band{left:0;top:930px;width:902px;height:270px;background:var(--sky)}
.newsletter-title{left:101px;top:1002px;font-size:25px;font-weight:700;color:#222}
.email{left:99px;top:1039px;width:184px;height:31px;background:var(--white);border-radius:3px;font-size:13px;color:#666;padding:8px 16px}
.subscribe{left:293px;top:1039px;width:102px;height:31px;border-radius:3px;font-size:16px}

.quote{left:591px;top:874px;width:233px;height:211px;background:var(--white);border-radius:10px;border:1px solid #e0e0e0;padding:10px 0 0 26px;z-index:3}
.quote-head{display:flex;align-items:center;gap:4px;font-family:"Ubuntu",sans-serif;font-size:17px;color:var(--title-blue);margin-left:-9px;letter-spacing:.2px}
.quote-mark{font-family:"Tinos",serif;font-size:52px;line-height:34px;color:var(--title-blue);font-weight:700;height:30px}
.quote-lead{margin-top:10px;font-size:12px;line-height:14px;color:var(--title-blue)}
.quote-body{margin-top:13px;font-size:11.5px;line-height:14px;color:#444;white-space:nowrap}
.quote-name{margin-top:6px;font-size:12px;line-height:14px;color:var(--title-blue)}
.quote-role{font-size:12px;color:#444}
.quote-tail{z-index:3}

.foot-links{left:0;top:1116px;width:902px;text-align:center;font-size:9.5px;color:var(--white);letter-spacing:.2px}
.foot-links .copy{margin-top:6px;display:block}
</style>
</head>
<body>

<header>
  <div class="abs brand"><span class="brand-dot"></span>HARBORKITE</div>
  <div class="abs social top" aria-label="Social links"><span></span><span></span><span></span></div>
  <nav class="abs nav">
    <a class="current" style="width:65px">Home</a>
    <a style="width:64px">About Us</a>
    <a style="width:62px">Services</a>
    <a style="width:63px">SEO</a>
    <a style="width:61px">SEM</a>
    <a style="width:53px">Blog</a>
    <a style="width:65px">Contact</a>
  </nav>
  <div class="abs search"><div class="search-box">Search...<span class="search-btn"></span></div></div>
</header>

<section class="abs hero">
  <div class="hero-photo" role="img" aria-label="Hand holding a seedling in soil"></div>
  <svg style="position:absolute;left:0;top:0" width="902" height="318" viewBox="0 0 902 318">
    <g fill="#ffffff">
      <ellipse cx="140" cy="318" rx="55" ry="35"/>
      <ellipse cx="300" cy="330" rx="120" ry="80"/>
      <ellipse cx="380" cy="310" rx="60" ry="55"/>
      <ellipse cx="470" cy="330" rx="80" ry="45"/>
      <ellipse cx="600" cy="330" rx="100" ry="40"/>
      <ellipse cx="810" cy="320" rx="45" ry="25"/>
      <rect x="90" y="300" width="810" height="18"/>
    </g>
    <g fill="#6fd0f8">
      <circle cx="314" cy="190" r="3"/><circle cx="300" cy="205" r="3"/><circle cx="277" cy="227" r="5"/>
      <circle cx="338" cy="233" r="7"/><circle cx="468" cy="237" r="5"/><circle cx="505" cy="250" r="10"/>
      <circle cx="232" cy="259" r="3"/><circle cx="804" cy="190" r="3"/><circle cx="821" cy="226" r="7"/>
      <circle cx="853" cy="233" r="3"/><circle cx="880" cy="256" r="3"/><circle cx="843" cy="279" r="7"/>
    </g>
  </svg>
  <h1>HELPING YOUR<br>BUSINESS GROW</h1>
  <h2>Place your Business at the<br>top of Search Engines</h2>
  <a class="know btn-red">KNOW HOW</a>
</section>

<section>
  <div class="abs card-photo" style="left:86px;background:linear-gradient(135deg,#b9d3e3,#6f8493 60%,#c9d6dd)" role="img" aria-label="Two people pointing at an online marketing diagram"></div>
  <div class="abs card-photo" style="left:254px;background:linear-gradient(135deg,#f4f4f4,#d9d9d9 55%,#bdbdbd)" role="img" aria-label="Magnifying glass over a bar chart"></div>
  <div class="abs card-photo" style="left:415px;background:linear-gradient(135deg,#f1f1f1,#9a8f86 55%,#e8e8e8)" role="img" aria-label="Team of colleagues at a laptop"></div>

  <p class="abs card-text" style="left:87px">Aliquam congue fermentum<br>Mauris accumsan nulla vel.</p>
  <p class="abs card-text" style="left:258px">Aliquam congue fermentum<br>Mauris accumsan nulla vel.</p>
  <p class="abs card-text" style="left:419px">Aliquam congue fermentum<br>Mauris accumsan nulla vel.</p>

  <a class="abs btn-grey card-btn" style="left:118px">Learn More</a>
  <a class="abs btn-grey card-btn" style="left:289px">Learn More</a>
  <a class="abs btn-grey card-btn" style="left:450px">Learn More</a>
</section>

<aside>
  <h3 class="abs section-title news-title">Latest News</h3>
  <p class="abs news-sub">LOREM IPSU DOLOR SIT AMET.</p>
  <ul class="abs news-list">
    <li>Aliquam dapibus tincidunt metus donec sagittis</li>
    <li>Praesent justo dolor sagittis euismod purus</li>
    <li>Vestibulum sed ante</li>
    <li>Donec sagittis euismod purus</li>
    <li>Praesent justo dolor sagittis euismod purus</li>
  </ul>
  <a class="abs btn-red news-btn">Read More</a>
</aside>

<section>
  <h3 class="abs about-title">About Harborkite</h3>
  <div class="abs about-text">
    <p>Aliquam congue fermentum nisl. Mauris accumsan nulla vel diam.<br>Sed in lacus ut enim adipiscing aliquet.</p>
    <p>Nulla venenatis. In pede mi, aliquet sit amet, euismod in, auctor<br>ut, ligula. Aliquam dapibus tincidunt metus. Praesent justo dolor,<br>lobortis quis, lobortis dignissim, pulvinar ac, lorem. Vestibulum<br>sed ante. Donec sagittis euismod purus.</p>
  </div>
  <a class="abs btn-grey about-btn">Read More</a>
</section>

<aside>
  <h3 class="abs section-title blog-title">Recent from Blog</h3>
  <ul class="abs blog-list">
    <li>Aliquam congue fermentum nisl. Mauris accumsan nulla vel diam.</li>
    <li class="short">Aliquam congue fermentum nisl. .</li>
    <li>Aliquam congue fermentum nisl. Mauris accumsan nulla vel diam.</li>
    <li class="short">Aliquam congue fermentum nisl. .</li>
  </ul>
</aside>

<footer>
  <div class="abs backdrop footer-band"></div>
  <svg class="abs backdrop" style="left:0;top:900px" width="902" height="140" viewBox="0 0 902 140" aria-hidden="true">
    <g fill="#ffffff">
      <rect x="0" y="0" width="902" height="30"/>
      <ellipse cx="120" cy="25" rx="35" ry="25"/>
      <ellipse cx="200" cy="35" rx="80" ry="45"/>
      <ellipse cx="330" cy="40" rx="75" ry="42"/>
      <ellipse cx="440" cy="45" rx="80" ry="55"/>
      <ellipse cx="560" cy="60" rx="70" ry="80"/>
      <ellipse cx="650" cy="60" rx="60" ry="70"/>
      <ellipse cx="835" cy="30" rx="40" ry="25"/>
    </g>
    <g fill="#6fd0f8">
      <circle cx="232" cy="75" r="3"/><circle cx="175" cy="95" r="3"/><circle cx="197" cy="100" r="5"/>
      <circle cx="242" cy="117" r="3"/><circle cx="278" cy="110" r="5"/><circle cx="338" cy="113" r="7"/>
      <circle cx="468" cy="110" r="5"/><circle cx="505" cy="95" r="10"/><circle cx="528" cy="117" r="5"/>
      <circle cx="843" cy="55" r="7"/><circle cx="880" cy="77" r="3"/><circle cx="853" cy="100" r="3"/>
    </g>
  </svg>
  <svg class="abs backdrop" style="left:0;top:1000px" width="902" height="120" viewBox="0 0 902 120" aria-hidden="true">
    <g fill="#6fd0f8">
      <circle cx="300" cy="60" r="3"/><circle cx="821" cy="7" r="7"/><circle cx="804" cy="100" r="3"/>
    </g>
  </svg>

  <h3 class="abs newsletter-title">Newsletter</h3>
  <div class="abs email">Email Address:</div>
  <a class="abs btn-red subscribe">Subscribe</a>

  <blockquote class="abs quote">
    <div class="quote-head"><span class="quote-mark">&ldquo;</span>Satisfied Customer</div>
    <p class="quote-lead">Lorem ipsum dolor sit amet,<br>consectetuer adipiscing elit.</p>
    <p class="quote-body">Praesent vestibulum molestie<br>lacus. Aenean&nbsp; nonummy<br>hendrerit mauris. Phasellus<br>porta. Fusce cmi.</p>
    <p class="quote-name">Dana Whitlow</p>
    <p class="quote-role">Director, Lindale Marketing</p>
  </blockquote>
  <svg class="abs quote-tail" style="left:772px;top:1083px" width="20" height="20" viewBox="0 0 20 20" aria-hidden="true">
    <path d="M2 0 L18 0 L5 18 Z" fill="#ffffff"/>
  </svg>
  <div class="abs social foot" aria-label="Social links"><span></span><span></span><span></span></div>

  <div class="abs foot-links">
    Home &nbsp;|&nbsp; About Us &nbsp;|&nbsp; Services &nbsp;|&nbsp; SEO &nbsp;|&nbsp; SEM &nbsp;|&nbsp; Blog &nbsp;|&nbsp; Contact
    <span class="copy">HARBORKITE &nbsp;© 2012.&nbsp; All Rights Reserved</span>
  </div>
</footer>

</body>
</html>
```